Iconic Cool Labels for Amazing Coffee

I'm back again after a very successful logo design project, now looking for label designs!

NOTEs:

IF YOU SUBMIT A DESIGN YOU WILL DEFINITELY RECEIVE FEEDBACK. I think it's rude not to respond when somebody takes the time to devote their time and talent to a project like this.

THIS BRIEF IS LONG. Out of respect for you, the designers. I've put a lot of time into this to give you as much understanding as I can. I think if you are going to invest your time it is only right and proper that I do the same. So please don't be put off by the length - it is intended to save you time and energy.

THE BRIEF

We are launching a coffee website called Brewvantia aimed at those who really care about coffee and have a passion for getting the very best out of it. So far, we have a great logo (attached), we have the website under construction and with the look and feel decided.

We are not a mass market player - instead we are more like an online boutique. But, we are starting out and need to look chic in a way that doesn't involve large investments. So, our coffee will be packaged in bags (1kg and 250g) with brown paper exteriors (brown kraft) onto which we'll put self adhesive labels.This is where we need your help.

THE TASK
- Create the 2 "master" labels for the front of the bags
- Create the variety labels that go either on or somewhere around the master label
- Create a small label for the back of the bag that contains the required regulatory information

There are 2 "families" - each requiring a family label. They are our blends (there are 7 of these), our single origin coffees (there are 3 of these) and the fair trade organic.

MASTER LABELS - In my mind the main focus of this brief
For the front of the bag there will be a master label for each of the 2 families, with another self-adhesive label placed either on top of the master label or adjacent to it. The exception being the free trade organic - there is only one of these, so no over labelling required.

The master labels are the main game here. They need to be distinctive and tasteful. They should look "chic" but not "try hard". They should be different to each other yet clearly part of the same house.

Both master labels MUST include the Brewvantia logo (supplied) and must also include a small Tessaro logo somewhere. Tessaro is our roaster. Perhaps it might be "Proudly roasted by (Tessaro logo)", or something like that.

The master labels are needed in each of the 1kg and 250g sizes and should have the size displayed as a part of the label.

The 2 master labels are:
Blends - these are beans from multiple origins and are typically used for espresso, late etc. I'd prefer that the label doesn't say "blends".

Single Origin - these are coffees from a single place in the world. They are for enthusiasts who want to explore the nuance and subtlety of a single region. Rather than be made in an espresso machine (although they can be) siphons are where these truly come in to their own.

VARIETY LABEL
These will either be stuck in a designated space on the MASTER LABEL or will be stuck somewhere else on the usable area. There are 7 of these in the blends family and 3 in the single origins family. They may be all very similar in look and feel or they may be variations within a theme. What do you think they should be?

You may decide to make them look similar of different. You might have groups - e.g. the first four, the free trade organics and the decafs. (Though if you do please don't do the cliched thing and make the decafs blue!)

Our Varieties are:
BLENDS
The Keystone
The Devotee
The Sybarite
The Reveller
Free Trade Organic
Swiss Decafeinated
Mexican Mountain Decafeinated

SINGLE ORIGIN
Ethiopian Garsu
Costa Rica El Pinar
Nicaraguan Tolvanera Superior

COMPLIANCE LABEL
This is a small label to go onto the back of the bag for all of our coffees. It contains all of the regulatory and compliance information. I'd like this to be small and reasonably unobtrusive, but clearly from the same "stable" as the other labels. This should be a regular shape so it's easy and quick to stick on, but not necessarily a rectangle - you pick.

It should contain:

Brewvantia
PO Box 4736
Larvik VIC 3902
www.brewvantia-example.com.au

Roasted, Blended & Packed in Australia
from Imported Beans

Store away from sunlight in a cool dry place

TECHNICAL DETAILS
The usable areas are (in portrait format)
1kg - 180mm high by 100mm wide
250g - 140mm high by 70mm wide

How much of this space you use and how you use it is up to you. My ingoing feeling is that using all of the available space would make it look "mass market" rather than premium. On the front, maybe there are a couple of small labels that are spaced, maybe there's one big label with an over sticker. I don't want to constrain you too much in this regard - except to say that unusual shapes like stars may be both slow and awkward to put onto the bags

THE CREATIVE SIDE
This is where you come in...
- Do you use all the space of just some of it (my guess is the latter)?
- One master on the front with an oversticker for variety or 2 separate labels?
- Rectangular labels or another shape (not jagged shapes please - too hard to stick evenly)
- Does the label contain, just words or does it have images, photos etc?
- Are the variety labels all similar or do they have a different look and feel?

ATTACHMENTS
- Brewvantia logo pack in zip file
- Tessaro logo
- Some photos I shared for the logo brief as examples
Updates

All, 

The files I thought I'd attached didn't get there the first time. I think I've corrected that now. Sorry for any hassle caused.

Cheers,
Joe

Target Market(s)

Our target customers have one thing in common - they are passionate about excellent coffee. While they come from all walks of life the image in my head is of young professionals that wear designer clothes - lots of black - and are passionate about design. They aspire to have Halvor furniture and care passionately about both design and functionality. They go to the cinema, but mainly arthouse and foreign. They visit the theatre and art galleries. They care about their coffee and the making of it might even be described as a ritual. They have separate grinders and espresso machines and are especially particular about everything to do with coffee - the beans (where they come from and how they are roasted), the grind, the making of the coffee itself, right down to the cups and glasses in which they are served.

Industry/Entity Type

Construction

Requirements
Must have
• A look and feel of premiumness without being staid. I think companies that have done this incredible well include Velmor, Quiso, Tavrel, Dorfu, KTZ. They are clearly premium, but have a feeling of what I describe as understated cutting edge about them. There is a lot of work that has gone into all of their graphic material yet they don't look "try hard".The colour palate is quite narrow - black, white, silver/chrome, and various coffee shades ranging perhaps from the golden brown of the crema to the rich dark brown of a roasted bean.
Nice to have
• I would like the coffee bag to be something that people leave out because it looks cool an chic.
Should not have
• Please avoid the cliches. I was thrilled with the creativity in the logo work, so I am enthusiastic at the prospect of seeing the same here.

Importantly, please avoid steaming cups at all costs! Also, pictures of people sipping coffee and looking blissfully content are not what I'm looking for.

Also, out emphasis is italian style coffee - espresso, late etc rather than the long black coffee that comes out of a filter machine that is popular in the US - consequently images that connote that should be avoided.

```html
<!DOCTYPE html>
<html lang="en">
<head>
<meta charset="utf-8">
<title>Brewvantia – Master Labels</title>
<link rel="stylesheet" href="https://fonts.googleapis.com/css2?family=Anton&family=Oswald:wght@300;600&display=swap">
<style>
  :root {
    --page: #ffffff;
    --kraft: #c7a674;
    --kraft-stripe: #bf9d6b;
    --kraft-light: rgba(236, 214, 176, 0.28);
    --ink: #1c1510;
    --mark: #2b1a11;
    --ornament-light: #f1e3c8;
    --ornament-mid: #dcc29a;
  }
  * { margin: 0; padding: 0; box-sizing: border-box; }
  html, body { width: 1200px; height: 900px; overflow: hidden; background: var(--page); }
  .canvas { position: relative; width: 1200px; height: 900px; }

  .label {
    position: absolute;
    top: 16px;
    width: 480px;
    height: 860px;
    background-color: var(--kraft);
    background-image: repeating-linear-gradient(90deg, transparent 0 5px, var(--kraft-stripe) 5px 6px, transparent 6px 11px);
    color: var(--ink);
    text-align: center;
  }
  .label--blend { left: 64px; }
  .label--origin { left: 654px; }

  .label__panel {
    position: absolute;
    left: 52px; top: 124px;
    width: 376px; height: 700px;
    background: var(--kraft-light);
  }

  .brand { position: absolute; left: 0; right: 0; top: 176px; }
  .brand__dot {
    display: block;
    width: 48px; height: 48px;
    margin: 0 auto;
    border-radius: 50%;
    background: var(--mark);
  }
  .brand__name {
    margin-top: 22px;
    font-family: "Oswald", sans-serif;
    font-weight: 300;
    font-size: 15px;
    letter-spacing: 0.5em;
    padding-left: 0.5em;
    text-transform: uppercase;
  }

  .artwork { position: absolute; }
  .artwork--burst {
    left: 170px; top: 286px;
    width: 140px; height: 140px;
    border-radius: 50%;
    background: radial-gradient(circle, var(--ornament-mid) 0 12%, var(--ornament-light) 22%, var(--ornament-mid) 48%, transparent 72%);
    opacity: 0.85;
  }
  .artwork--map {
    left: 110px; top: 290px;
    width: 260px; height: 130px;
    border-radius: 40% 45% 35% 50%;
    background: radial-gradient(ellipse at 50% 45%, var(--ornament-light) 0 45%, var(--ornament-mid) 75%, transparent 100%);
    opacity: 0.85;
  }

  .family {
    position: absolute; left: 0; right: 0; top: 446px;
    font-family: "Anton", sans-serif;
    font-size: 40px;
    line-height: 1;
    font-weight: 400;
  }
  .copy {
    position: absolute; left: 60px; right: 60px;
    font-family: "Oswald", sans-serif;
    font-weight: 600;
    font-size: 12.5px;
    line-height: 24px;
    letter-spacing: 0.02em;
    text-transform: uppercase;
  }
  .copy--family { top: 506px; }
  .copy--variety { top: 654px; }

  .roaster { white-space: nowrap; }
  .roaster__dot {
    display: inline-block;
    width: 9px; height: 9px;
    border-radius: 50%;
    background: var(--ink);
    margin: 0 3px 0 2px;
    vertical-align: 0;
  }

  .variety {
    position: absolute; left: 0; right: 0;
    font-family: "Anton", sans-serif;
    font-weight: 400;
    line-height: 1;
    text-transform: uppercase;
  }
  .variety--prefix { top: 712px; font-size: 26px; }
  .variety--name { top: 744px; font-size: 46px; }
  .variety--country { top: 720px; font-size: 46px; }
  .variety--estate { top: 772px; font-size: 24px; }
</style>
</head>
<body>
<main class="canvas">

  <section class="label label--blend">
    <div class="label__panel"></div>
    <div class="brand">
      <span class="brand__dot"></span>
      <p class="brand__name">Brewvantia</p>
    </div>
    <div class="artwork artwork--burst" role="img" aria-label="Radiating dotted burst ornament"></div>
    <h2 class="family">SPECIAL BLEND</h2>
    <p class="copy copy--family">Hand selected varieties blended in<br>unique and surprising combinations<br><span class="roaster">Roasted in Australia by <span class="roaster__dot"></span>Tessaro &nbsp;1 KG</span></p>
    <p class="copy copy--variety">Aenean in mollis ipsum curabitur<br>sedoli malesuada risus mauris</p>
    <p class="variety variety--prefix">The</p>
    <h1 class="variety variety--name">Keystone</h1>
  </section>

  <section class="label label--origin">
    <div class="label__panel"></div>
    <div class="brand">
      <span class="brand__dot"></span>
      <p class="brand__name">Brewvantia</p>
    </div>
    <div class="artwork artwork--map" role="img" aria-label="Pale world map showing coffee growing regions"></div>
    <h2 class="family">SINGLE ORIGIN</h2>
    <p class="copy copy--family">Painstakingly selected regional<br>variations from around the world<br><span class="roaster">Roasted in Australia by <span class="roaster__dot"></span>Tessaro &nbsp;1 KG</span></p>
    <p class="copy copy--variety">Rich blended nuts sweet mellow<br>peach and a trace of chocolate</p>
    <h1 class="variety variety--country">Costa Rica</h1>
    <p class="variety variety--estate">El Pinar</p>
  </section>

</main>
</body>
</html>
```